Bright Arch Group business card

Bright Arch Group is the parent company of Bright Arch Building, Bright Arch Plumbing and Bright Arch Renovating. We require a sophisticated business card that covers all aspects of the building and plumbing space without using told or construction items.

Industry/Entity Type

Construction Company

Contact Information for Business Card

Gareth Pimley
Director
0472915083
gareth@brightarch.com.au
Www.brightarch.com.au

Font styles to use
Serif
Sans Serif

Colors
3176b5
ffce3e
0692cd
34a7d8
fbee3e
faa54b

Requirements
Must have
• Logo on front
• Logo and details on rear.
Nice to have
• Maybe water mark or shadow effect with logo
Should not have
• Tools or any construction associated items

```html
<!DOCTYPE html>
<html lang="en">
<head>
<meta charset="utf-8">
<title>Bright Arch Group – Business Card</title>
<link rel="stylesheet" href="https://fonts.googleapis.com/css2?family=Jost:wght@400&family=Oswald:wght@500&family=Lato:wght@400&display=swap">
<style>
  :root {
    --page-bg: #e9e6e2;
    --card-white: #ffffff;
    --card-black: #000000;
    --accent-orange: #f47f20;
    --ink-dark: #111111;
    --ink-grey: #555555;
    --rule-grey: #8a8a8a;
    --ink-light: #ffffff;
  }
  * { margin: 0; padding: 0; box-sizing: border-box; }
  html, body { width: 1200px; height: 960px; overflow: hidden; }
  body {
    background: var(--page-bg);
    position: relative;
    font-family: "Lato", sans-serif;
  }
  .card {
    position: absolute;
    left: 257px;
    width: 703px;
    height: 401px;
    overflow: hidden;
  }
  .card--front { top: 52px; background: var(--card-white); }
  .card--back { top: 508px; background: var(--card-black); }

  /* Brand name (stands in for the mark) */
  .brand {
    position: absolute;
    display: flex;
    align-items: center;
    gap: 14px;
  }
  .brand__dot {
    width: 22px; height: 22px;
    border-radius: 50%;
    background: var(--accent-orange);
  }
  .brand__name {
    font-family: "Jost", sans-serif;
    font-weight: 400;
    letter-spacing: 5px;
    white-space: nowrap;
  }
  .card--front .brand { right: 42px; top: 88px; }
  .card--front .brand__name { font-size: 30px; color: var(--ink-dark); }
  .card--back .brand { left: 0; right: 0; top: 218px; justify-content: center; }
  .card--back .brand__name { font-size: 40px; color: var(--ink-light); letter-spacing: 7px; }

  /* Front: identity block */
  .tab {
    position: absolute;
    left: 0; top: 194px;
    width: 16px; height: 66px;
    background: var(--accent-orange);
    border-radius: 0 14px 14px 0;
  }
  .person { position: absolute; left: 50px; top: 200px; }
  .person__name {
    font-family: "Oswald", sans-serif;
    font-weight: 500;
    font-size: 30px;
    line-height: 1.1;
    color: var(--accent-orange);
    transform: scaleX(0.88);
    transform-origin: left;
  }
  .person__role { font-size: 20px; color: var(--ink-grey); margin-top: 2px; }
  .divider {
    position: absolute;
    left: 50px; top: 278px;
    width: 612px; height: 1px;
    background: var(--rule-grey);
  }
  .contacts { position: absolute; left: 50px; top: 305px; list-style: none; }
  .contacts__item {
    display: flex; align-items: center; gap: 11px;
    font-size: 17px; color: var(--ink-grey);
    height: 22.5px;
  }
  .contacts__icon { width: 18px; height: 18px; flex: none; }

  .card--back .website {
    position: absolute;
    left: 0; right: 0; top: 352px;
    text-align: center;
    font-size: 15px;
    letter-spacing: 3px;
    color: var(--ink-light);
  }
</style>
</head>
<body>
  <section class="card card--front" aria-label="Card front">
    <div class="brand">
      <span class="brand__dot"></span>
      <span class="brand__name">BRIGHT ARCH GROUP</span>
    </div>
    <div class="tab"></div>
    <div class="person">
      <h1 class="person__name">GARETH PIMLEY</h1>
      <p class="person__role">Director</p>
    </div>
    <div class="divider"></div>
    <ul class="contacts">
      <li class="contacts__item">
        <svg class="contacts__icon" viewBox="0 0 18 18" aria-hidden="true">
          <rect width="18" height="18" rx="4" fill="#f47f20"/>
          <path d="M6 4.5c.8-.5 1.4 0 1.7.8l.4 1.2c.1.5-.2.9-.6 1.1-.3.2-.3.5-.2.8.5 1.2 1.3 2 2.4 2.6.3.1.6.1.8-.2.3-.4.7-.6 1.2-.4l1.1.5c.7.3 1 1 .5 1.7-.7.9-1.9 1.3-3 .8C7.9 12.4 5.5 10 4.5 7.6c-.4-1.2 0-2.4 1.5-3.1z" fill="#fff"/>
        </svg>
        <span>0472915083</span>
      </li>
      <li class="contacts__item">
        <svg class="contacts__icon" viewBox="0 0 18 18" aria-hidden="true">
          <rect width="18" height="18" rx="4" fill="#f47f20"/>
          <rect x="4" y="5.5" width="10" height="7" rx="1" fill="none" stroke="#fff" stroke-width="1.3"/>
          <path d="M4.5 6l4.5 3.5L13.5 6" fill="none" stroke="#fff" stroke-width="1.3"/>
        </svg>
        <span>gareth@brightarch.com.au</span>
      </li>
      <li class="contacts__item">
        <svg class="contacts__icon" viewBox="0 0 18 18" aria-hidden="true">
          <rect width="18" height="18" rx="4" fill="#f47f20"/>
          <circle cx="9" cy="9" r="5" fill="none" stroke="#fff" stroke-width="1.2"/>
          <ellipse cx="9" cy="9" rx="2.2" ry="5" fill="none" stroke="#fff" stroke-width="1.1"/>
          <path d="M4 9h10" stroke="#fff" stroke-width="1.1"/>
        </svg>
        <span>www.brightarch.com.au</span>
      </li>
    </ul>
  </section>

  <section class="card card--back" aria-label="Card back">
    <div class="brand">
      <span class="brand__dot"></span>
      <span class="brand__name">BRIGHT ARCH GROUP</span>
    </div>
    <p class="website">www.brightarch.com.au</p>
  </section>
</body>
</html>
```